Lorn & Vell Designs - Promotions flyer

I am a locally based Interior designer /stylist on Sydney's lower north shore. I would like to offer my services:
Full Professional Styling Services and Furniture Hire
Colour Consultation – Interior / exterior
Floor Coverings
Furniture selection and sourcing
Window Treatments
Wallpaper
Soft Furnishings
Upholstery
Renovations

I would like to offer a free consultation
Updates

Project Deadline Extended
Reason: I've been speaking with a designer and need her to make one more change. I have tried to message her twice, but have had no reply. Once she makes these changes I'm ready to sign off on the design. Thanks Harriet

Target Market(s)

30 - 60's middle to high income earners

Industry/Entity Type

Floor

Requirements
Must have
• one sided DL size
Use my logo
1 or 2 images of interior space or image of a lamp, cushion, lounge etc
The following contact details:
Mobile: 041 xxx xxxx
Website Address: www.lornandvelldesigns.example.au

```html
<!DOCTYPE html>
<html lang="en">
<head>
<meta charset="utf-8">
<title>Lorn &amp; Vell Designs – Services Flyer</title>
<link rel="stylesheet" href="https://fonts.googleapis.com/css2?family=Lato:wght@300;400;700&family=Pacifico&display=swap">
<style>
  :root {
    --page-bg: #e9e7e4;
    --orange: #f29a57;
    --brown: #7b4a12;
    --wall: #ffffff;
    --wall-shade: #f1f0ee;
    --floor: #c9c4be;
    --floor-dark: #b7b1aa;
    --ink-grey: #5e5a57;
    --white: #ffffff;
  }
  html, body {
    margin: 0;
    width: 1200px;
    height: 750px;
    overflow: hidden;
    background: var(--page-bg);
  }
  .canvas {
    position: relative;
    width: 1200px;
    height: 750px;
  }
  .flyer {
    position: absolute;
    left: 70px;
    top: 125px;
    width: 1060px;
    height: 500px;
    background: var(--wall);
    box-shadow: 0 10px 30px rgba(0,0,0,0.18);
    overflow: hidden;
    font-family: "Lato", sans-serif;
  }
  .interior-photo {
    position: absolute;
    inset: 0;
    background:
      radial-gradient(ellipse 120px 170px at 810px 330px, rgba(90,70,55,0.55), rgba(90,70,55,0) 75%),
      linear-gradient(to bottom, var(--wall) 0%, var(--wall-shade) 58%, var(--floor) 62%, var(--floor-dark) 100%);
  }
  .services-panel {
    position: absolute;
    left: 0;
    top: 0;
    width: 440px;
    height: 500px;
    background: var(--orange);
    border-left: 10px solid var(--brown);
    box-sizing: border-box;
  }
  .services-heading {
    margin: 22px 0 8px 34px;
    font-family: "Pacifico", cursive;
    font-weight: 400;
    font-size: 40px;
    line-height: 1.2;
    color: var(--white);
  }
  .services-list {
    list-style: none;
    margin: 0;
    padding: 0 30px 0 34px;
    color: var(--white);
    font-weight: 300;
    font-size: 18px;
    line-height: 1.32;
  }
  .services-list li {
    position: relative;
    padding-left: 22px;
  }
  .services-list li::before {
    content: "";
    position: absolute;
    left: 0;
    top: 7px;
    width: 10px;
    height: 10px;
    background: var(--white);
  }
  .call-band {
    position: absolute;
    left: 0;
    right: 0;
    bottom: 0;
    height: 86px;
    background: var(--brown);
    padding: 12px 0 0 34px;
    box-sizing: border-box;
    color: var(--white);
  }
  .call-line {
    font-size: 30px;
    font-weight: 400;
    letter-spacing: 0.5px;
    line-height: 1;
  }
  .call-label {
    color: var(--orange);
    font-size: 20px;
    margin-right: 6px;
  }
  .offer-line {
    margin-top: 8px;
    font-size: 15px;
    font-weight: 300;
  }
  .offer-line strong {
    font-weight: 700;
    letter-spacing: 0.4px;
  }
  .brand-name {
    position: absolute;
    right: 48px;
    top: 70px;
    margin: 0;
    font-family: "Lato", sans-serif;
    font-weight: 400;
    font-size: 36px;
    line-height: 1;
    color: var(--ink-grey);
  }
  .website {
    position: absolute;
    right: 48px;
    bottom: 20px;
    font-size: 22px;
    font-weight: 400;
    color: var(--ink-grey);
    letter-spacing: 0.3px;
  }
</style>
</head>
<body>
<div class="canvas">
  <article class="flyer">
    <div class="interior-photo" role="img" aria-label="Photograph of an upholstered French armchair with a patterned cushion against a white wall on a pale grey floor"></div>

    <section class="services-panel">
      <h2 class="services-heading">Services</h2>
      <ul class="services-list">
        <li>Full Professional Styling Services and Furniture Hire</li>
        <li>Colour Consultation – Interior / exterior</li>
        <li>Floor Coverings</li>
        <li>Furniture selection and sourcing</li>
        <li>Window Treatments</li>
        <li>Wallpaper</li>
        <li>Soft Furnishings</li>
        <li>Upholstery</li>
        <li>Renovations</li>
      </ul>
      <div class="call-band">
        <div class="call-line"><span class="call-label">CALL</span>041 xxx xxxx</div>
        <div class="offer-line">for <strong>FREE CONSULTATION</strong></div>
      </div>
    </section>

    <h1 class="brand-name">Lorn &amp; Vell Designs</h1>

    <div class="website">www.lornandvelldesigns.example.au</div>
  </article>
</div>
</body>
</html>
```